Events and Brand activation brochure

We are looking for a new Brochure. This Brochure's main focus is pictures (minimal text). I have attached the template including all the pictures and page titles we would like. We are working on the text at the moment however, we need a better idea of where to place the text. The pictures that are placed individually on a seperate page are to stay that way with no text. The pages with more than one picture on them, they can be created into a collage of some sort? We dont need much text space as it will mainly be bullet points. We would like a cool looking map on the back showcasing all of our locations as shown in the template.
Please follow our Logo design throughout the pages which is also uploaded.
The Brochure should be more of a booklet (LANDSCAPE- 24cmX25cm)

Industry/Entity Type

Events

Colors
3276b5
85acd3
0555a3
85cae6

Requirements
Must have
• Landscape
• Booklet
Nice to have
• Include one of the Kestrel Arch pictures faded out as background for ''about us page''??

```html
<!DOCTYPE html>
<html lang="en">
<head>
<meta charset="utf-8">
<title>Aerona – Events and Brand Activation Brochure</title>
<link rel="stylesheet" href="https://fonts.googleapis.com/css2?family=Open+Sans:wght@300;400;600;700;800&display=swap">
<style>
:root{
  --stage:#c7c6ce;
  --stage-dark:#a9a8b3;
  --page-brown:#6e5d3c;
  --page-brown-dark:#4d4129;
  --sepia-light:#c9a873;
  --sepia-mid:#8c6e43;
  --sepia-dark:#3d301d;
  --accent:#e9a23b;
  --navy:#1f3f78;
  --brand-blue:#3276b5;
  --brand-sky:#85cae6;
  --brand-soft:#85acd3;
  --paper:#ffffff;
  --ink:#2a2a2a;
  --text-light:#efe3cc;
}
*{box-sizing:border-box;margin:0;padding:0}
html,body{width:1200px;height:750px;overflow:hidden}
body{
  font-family:"Open Sans",Arial,sans-serif;
  background:linear-gradient(160deg,var(--stage) 0%,var(--stage-dark) 100%);
  position:relative;
}
.spread{
  position:absolute;width:540px;height:320px;display:flex;
  box-shadow:0 10px 24px rgba(0,0,0,.35);
}
.spread--cover{left:30px;top:28px}
.spread--about{left:630px;top:28px}
.spread--events{left:30px;top:403px}
.spread--branding{left:630px;top:403px}
.page{position:relative;width:270px;height:320px;overflow:hidden}
.page--brown{background:linear-gradient(135deg,var(--page-brown) 0%,var(--page-brown-dark) 100%)}
.spread--events .page--brown,.spread--branding .page--brown{width:540px}
.gutter{position:absolute;left:269px;top:0;width:2px;height:100%;background:rgba(0,0,0,.25);z-index:5}

/* back cover */
.page--back{background:var(--paper)}
.back-logo{position:absolute;left:22px;top:22px;display:flex;align-items:center;gap:6px;z-index:2}
.logo-dot{width:12px;height:12px;border-radius:50%;background:var(--brand-blue)}
.logo-name{font-weight:700;font-size:13px;letter-spacing:3px;color:var(--brand-blue)}
.map{position:absolute;left:112px;top:48px;width:146px;height:168px;border-radius:6px;
  background:radial-gradient(ellipse at 55% 50%,#7b8290 0%,#a3a8b1 60%,#e7e8ec 100%)}
.office{position:absolute;left:22px;font-size:6.5px;line-height:1.45;color:var(--ink);padding-left:10px}
.office::before{content:"";position:absolute;left:0;top:2px;width:6px;height:6px;border-radius:50% 50% 50% 0;transform:rotate(-45deg);background:var(--accent)}
.office--bcn{top:80px}
.office--ber{top:130px}
.contact-band{position:absolute;left:0;bottom:0;width:100%;height:90px;background:var(--navy);color:#fff;padding:14px 22px}
.contact-title{font-size:12px;font-weight:700;letter-spacing:.5px}
.contact-title span{font-weight:300}
.contact-rule{width:70px;height:2px;background:var(--accent);margin:4px 0 8px}
.contact-grid{display:flex;gap:26px;font-size:7px;line-height:1.6}
.contact-grid strong{font-weight:700}
.contact-email{position:absolute;right:16px;bottom:8px;font-size:6.5px;color:#dfe6f3}

/* front cover */
.cover-photo{position:absolute;inset:0;background:linear-gradient(170deg,var(--sepia-mid) 0%,var(--sepia-light) 45%,var(--sepia-dark) 100%)}
.cover-logo{position:absolute;right:22px;top:128px;text-align:center}
.cover-logo .brand{display:flex;align-items:center;gap:7px;justify-content:center}
.cover-logo .logo-name{font-size:18px;letter-spacing:5px;color:var(--navy)}
.cover-logo .logo-dot{width:14px;height:14px;background:var(--navy)}
.tagline{font-size:6.5px;letter-spacing:1.5px;color:var(--navy);margin-top:3px}

/* inner pages */
.page-title{position:absolute;left:26px;top:30px;color:#fff;font-size:17px;line-height:1.1}
.page-title b{font-weight:800}
.page-title span{font-weight:300}
.title-rule{position:absolute;left:26px;width:120px;height:2px;background:var(--accent)}
.body-copy{position:absolute;left:26px;width:190px;font-size:6.5px;line-height:1.55;color:var(--text-light)}
.body-copy p+p{margin-top:8px}
.footer{position:absolute;left:26px;bottom:14px}
.footer-rule{width:90px;height:1px;background:var(--accent);margin-bottom:6px}
.footer-web{display:flex;align-items:center;gap:5px;font-size:6.5px;color:#f1e6d0}
.footer-dot{width:7px;height:7px;border-radius:50%;background:var(--accent)}
.footer-web b{font-weight:700}
.about-photo{position:absolute;inset:0;background:radial-gradient(ellipse at 50% 40%,#e6dccb 0%,#b49c78 40%,#4a3c27 100%)}

.collage-photo{position:absolute;box-shadow:0 2px 6px rgba(0,0,0,.4)}
</style>
</head>
<body>

<!-- Spread 1: back and front cover -->
<section class="spread spread--cover">
  <div class="page page--back">
    <div class="back-logo"><span class="logo-dot"></span><span class="logo-name">AERONA</span></div>
    <div class="map" role="img" aria-label="Map of Europe marking the company locations"></div>
    <p class="office office--bcn">Carrer del Molí 14<br>Polígon Nord<br>08040 Barcelona<br>SPAIN</p>
    <p class="office office--ber">Lindenweg 27<br>10405 Berlin<br>GERMANY</p>
    <div class="contact-band">
      <h2 class="contact-title">CONTACT <span>US</span></h2>
      <div class="contact-rule"></div>
      <div class="contact-grid">
        <p><strong>+44 (0)20 7946 0182</strong><br>www.<strong>aerona</strong>.uk.com</p>
        <p>Unit 8 Riverside Works<br>Dock Road, London<br>E16 4QT</p>
      </div>
      <p class="contact-email">hello@aerona.uk.com</p>
    </div>
  </div>
  <div class="page page--front">
    <div class="cover-photo" role="img" aria-label="Sepia photograph of the Kestrel Arch wheel against a cloudy sky"></div>
    <div class="cover-logo">
      <div class="brand"><span class="logo-dot"></span><span class="logo-name">AERONA</span></div>
      <p class="tagline">Visual Impact From Above</p>
    </div>
  </div>
  <div class="gutter"></div>
</section>

<!-- Spread 2: about us -->
<section class="spread spread--about">
  <div class="page page--brown">
    <h2 class="page-title"><b>ABOUT</b> <span>US</span></h2>
    <div class="title-rule" style="top:54px"></div>
    <div class="body-copy" style="top:70px">
      <p>Aerona creates high impact visuals for events, venues and brands across Europe, from early concept through print and installation on site.</p>
      <p>Our crews work at height and at scale, delivering safe, fast and precise builds for stadiums, arenas and city landmarks.</p>
    </div>
    <div class="footer">
      <div class="footer-rule"></div>
      <div class="footer-web"><span class="footer-dot"></span><span>www.<b>aerona</b>.uk.com</span></div>
    </div>
  </div>
  <div class="page">
    <div class="about-photo" role="img" aria-label="Faded sepia photograph of the Kestrel Arch wheel beside riverside buildings"></div>
  </div>
  <div class="gutter"></div>
</section>

<!-- Spread 3: event management -->
<section class="spread spread--events">
  <div class="page page--brown">
    <h2 class="page-title"><b>EVENT</b> <span>MANAGEMENT</span></h2>
    <div class="title-rule" style="top:54px"></div>
    <div class="body-copy" style="top:68px">
      <p>Full venue dressing for major sporting and public events, including fence wraps, entrance arches, signage and wayfinding planned around every crowd flow.</p>
    </div>
    <div class="collage-photo" role="img" aria-label="Photo of pink and blue venue wraps on scaffolding" style="left:26px;top:150px;width:180px;height:110px;background:linear-gradient(135deg,#d6478f,#3b73c4)"></div>
    <div class="collage-photo" role="img" aria-label="Photo of blue branded hoardings at an event site" style="left:228px;top:98px;width:90px;height:82px;background:linear-gradient(135deg,#5e7fa8,#a7b4c2)"></div>
    <div class="collage-photo" role="img" aria-label="Photo of a white venue facade with printed panels" style="left:275px;top:70px;width:60px;height:84px;background:linear-gradient(135deg,#cfd4d9,#8d9399)"></div>
    <div class="collage-photo" role="img" aria-label="Photo of an event entrance with large banners under blue sky" style="left:312px;top:0;width:228px;height:118px;background:linear-gradient(180deg,#7eb0e3,#d9e3ea 60%,#9aa6a2)"></div>
    <div class="collage-photo" role="img" aria-label="Photo of a red branded entrance gate beside white tents" style="left:290px;top:156px;width:125px;height:116px;background:linear-gradient(160deg,#a9c8ea,#d9442e 60%,#b43625)"></div>
    <div class="collage-photo" role="img" aria-label="Photo of a purple scaffold wrap at a sports venue" style="left:430px;top:128px;width:110px;height:148px;background:linear-gradient(160deg,#8fb7e0,#9b3a9a 50%,#6a2a70)"></div>
    <div class="footer">
      <div class="footer-rule"></div>
      <div class="footer-web"><span class="footer-dot"></span><span>www.<b>aerona</b>.uk.com</span></div>
    </div>
  </div>
  <div class="gutter"></div>
</section>

<!-- Spread 4: branding and high impact graphics -->
<section class="spread spread--branding">
  <div class="page page--brown">
    <h2 class="page-title"><b>BRANDING AND</b><br><span>HIGH IMPACT GRAPHICS</span></h2>
    <div class="title-rule" style="top:70px"></div>
    <div class="body-copy" style="top:84px">
      <p>Building wraps, giant banners and bespoke displays that turn façades into landmarks and put your brand in front of thousands every day.</p>
    </div>
    <div class="collage-photo" role="img" aria-label="Photo of a red curved banner display on a building" style="left:150px;top:150px;width:160px;height:100px;background:linear-gradient(135deg,#b82a25,#e05a45)"></div>
    <div class="collage-photo" role="img" aria-label="Photo of a large orange promotional object in a red atrium" style="left:285px;top:12px;width:120px;height:112px;background:radial-gradient(circle at 45% 45%,#e78c2e,#9b1e16 70%)"></div>
    <div class="collage-photo" role="img" aria-label="Photo of a tall advertising wrap on a tower" style="left:325px;top:122px;width:100px;height:160px;background:linear-gradient(180deg,#b9c7d6,#3c4a63 50%,#27303f)"></div>
    <div class="collage-photo" role="img" aria-label="Photo of a giant building wrap under blue sky" style="left:428px;top:10px;width:112px;height:150px;background:linear-gradient(180deg,#7ea9d6,#c9a06a 55%,#8a6a45)"></div>
    <div class="collage-photo" role="img" aria-label="Photo of a three-dimensional product display on a grey wall" style="left:432px;top:176px;width:108px;height:90px;background:linear-gradient(135deg,#8e9296,#c8cbcf)"></div>
    <div class="footer">
      <div class="footer-rule"></div>
      <div class="footer-web"><span class="footer-dot"></span><span>www.<b>aerona</b>.uk.com</span></div>
    </div>
  </div>
  <div class="gutter"></div>
</section>

</body>
</html>
```